Veloran Dental Development - Business Cards

We are a Dental Development and Management company. We are looking to develop a new business card design. We are business professional but modern. The logo that I have attached is the business colors. You can also check out our website for further detail. www.veloranmgmt-example.com

Target Market(s)

Dental Professionals, Dentists and Office Staff, Marketing Professionals

Industry/Entity Type

Business

Requirements
Must have
• Name - Bartholomew K. Tressing
Title - Marketing Director
Phone - 555-019-4827
Cell - 555-019-4827
Email - Bart.t@veloran-example.com
Address - 2917 W Larkmoor Rd, Quillby Heights, QX 10427
Web- www.veloran-example.com

Veloran Logo must go on the front. The other logos go on the back as affiliated businesses

Must be editable to enter specific Names, Positions, Phone numbers and email later on. Using Adobe CS5 currently.

```html
<!DOCTYPE html>
<html lang="en">
<head>
<meta charset="utf-8">
<title>Veloran Dental Development – Business Card</title>
<link rel="stylesheet" href="https://fonts.googleapis.com/css2?family=Mulish:wght@300;400;600;700;800&display=swap">
<style>
  :root {
    --navy: #2a2c5c;
    --gold-glow: #f0d39a;
    --lavender: #8a84b6;
    --rule: #c9ad94;
    --white: #ffffff;
    --green-navy: #1f3d5a;
    --plan-red: #8e2424;
    --alert-red: #d0282e;
    --kid-blue: #2a9ad6;
  }
  html, body {
    margin: 0;
    padding: 0;
    width: 1050px;
    height: 1200px;
    overflow: hidden;
    background: var(--white);
    font-family: "Mulish", Arial, sans-serif;
    color: var(--navy);
  }
  .card-face {
    position: absolute;
    left: 0;
    width: 1050px;
    height: 600px;
    overflow: hidden;
  }
  .card-front {
    top: 0;
    border-bottom: 1px solid var(--navy);
    box-sizing: border-box;
    background:
      radial-gradient(ellipse 420px 300px at 930px 110px, var(--gold-glow) 0%, rgba(240,211,154,0.55) 40%, rgba(255,255,255,0) 100%),
      radial-gradient(ellipse 620px 420px at 40px 560px, var(--lavender) 0%, rgba(138,132,182,0.55) 45%, rgba(255,255,255,0) 100%),
      var(--white);
  }
  .card-back {
    top: 600px;
    background:
      radial-gradient(ellipse 640px 420px at 20px 600px, var(--lavender) 0%, rgba(138,132,182,0.5) 45%, rgba(255,255,255,0) 100%),
      linear-gradient(160deg, rgba(240,230,205,0.6) 0%, rgba(255,255,255,0) 35%),
      var(--white);
  }
  .company-name {
    position: absolute;
    left: 335px;
    top: 118px;
    margin: 0;
    font-weight: 700;
    color: var(--navy);
    line-height: 1;
  }
  .company-name .primary {
    display: block;
    font-size: 92px;
    letter-spacing: 1px;
  }
  .company-name .secondary {
    display: block;
    margin-top: 8px;
    margin-left: 46px;
    font-size: 36px;
    letter-spacing: 5px;
    text-transform: uppercase;
  }
  .contact-block {
    position: absolute;
    left: 381px;
    top: 330px;
    width: 530px;
  }
  .person-name {
    margin: 0;
    font-size: 37px;
    font-weight: 300;
    line-height: 44px;
  }
  .person-title {
    margin: 6px 0 0;
    font-size: 28px;
    font-weight: 700;
    letter-spacing: 1px;
    line-height: 36px;
  }
  .divider {
    margin: 18px 0 0;
    border: 0;
    border-top: 1px solid var(--rule);
  }
  .phones {
    margin: 20px 0 0;
    font-size: 26px;
    font-weight: 300;
    line-height: 34px;
  }
  .email {
    margin: 10px 0 0;
    font-size: 25px;
    font-weight: 600;
    line-height: 32px;
  }
  .affiliate {
    position: absolute;
    display: flex;
    align-items: center;
    gap: 10px;
    font-weight: 800;
    line-height: 1.05;
    text-align: center;
  }
  .affiliate-centers { left: 388px; top: 690px; width: 228px; font-size: 27px; color: var(--green-navy); justify-content: center; }
  .affiliate-plan { left: 655px; top: 690px; width: 256px; font-size: 27px; color: var(--plan-red); justify-content: center; }
  .affiliate-urgent { left: 382px; top: 818px; width: 240px; font-size: 24px; color: var(--alert-red); text-align: left; }
  .affiliate-urgent .mark {
    flex: none;
    width: 46px;
    height: 46px;
    background: var(--alert-red);
  }
  .affiliate-kids { left: 680px; top: 824px; width: 230px; font-size: 22px; color: var(--kid-blue); justify-content: center; text-align: left; }
  .affiliate-kids .mark {
    flex: none;
    width: 30px;
    height: 30px;
    border-radius: 50%;
    background: var(--kid-blue);
  }
  .back-details {
    position: absolute;
    left: 381px;
    top: 1058px;
  }
  .address {
    margin: 0;
    font-size: 26px;
    font-weight: 300;
    line-height: 34px;
  }
  .website {
    margin: 12px 0 0;
    font-size: 26px;
    font-weight: 600;
    letter-spacing: 1px;
    line-height: 34px;
  }
</style>
</head>
<body>
  <section class="card-face card-front">
    <h1 class="company-name">
      <span class="primary">Veloran</span>
      <span class="secondary">Dental Development</span>
    </h1>
    <div class="contact-block">
      <p class="person-name">Bartholomew K. Tressing</p>
      <p class="person-title">Marketing Director</p>
      <hr class="divider">
      <p class="phones">Phone: 555-019-4827 | Cell: 555-019-4827</p>
      <p class="email">Bart.t@veloran-example.com</p>
    </div>
  </section>

  <section class="card-face card-back"></section>

  <div class="affiliate affiliate-centers">Hearthstone Dental Centers</div>
  <div class="affiliate affiliate-plan">Hearthstone Dental Plan</div>
  <div class="affiliate affiliate-urgent"><span class="mark"></span><span>Urgentline Dental Centers</span></div>
  <div class="affiliate affiliate-kids"><span class="mark"></span><span>Sproutsmile Pediatric Dental</span></div>

  <div class="back-details">
    <p class="address">2917 W Larkmoor Rd, Quillby Heights, QX 10427</p>
    <p class="website">www.veloran-example.com</p>
  </div>
</body>
</html>
```